dentist office tri-fold for root canal specialist

design a tri fold brochure to give to patients talking about the office and the services
Talk about doctors and their bios
services: root canal , retreatments, endodontic surgery, trauma, cracked teeth
Technology: CBCT, microscopes, lasers, soft tide advanced
I will provide all the technical info. willing to hire a writer if needed. Attached a picture of our logo as a reference of our colors. Can attach older versions of brochure if requested. Looking for a very professional tri fold that will be used to market the practice to patients and other doctors.
Rough idea: TRIFOLD
Front Cover:
Welcome to The Pulpwell Clinic
Thank you for allowing us to care for your endodontic needs. We look forward to serving you.
We at The Pulpwell Clinic have dedicated our professional lives to improving the comfort and dental health of those in our care.
Inner Right:
Pics of Docs
Welcome – On behalf of our staff, we welcome you to our office.
We are pleased that you have selected our team of professionals to care for your endodontic needs. We want you to know that we are committed to providing you, our patient with the highest quality endodontic care in the most gentle, efficient, and caring manner possible. We pride ourselves on offering our expertise along with the best patient care with the most up to date technologies to better ensure your oral health.
For your convenience, please visit us online at www.pulpwellclinic.example for directions to our offices, pre and post-operative instructions, general information on our Endodontists and much more. We are here for you and our doctors are on call 24 hours a day, 7 days a week.
We are looking forward providing you a most relaxed and pleasant vist possible. Thank you again for choosing The Pulpwell Clinic.
Inner Middle:
What is a Root Canal?
A root canal (endodontic treatment) is one of the most common dental procedures performed, with more than 14 million performed every year. This simple treatment can save your natural teeth and prevent the need of dental implants or bridges.
At the center of your tooth is pulp. The pulp is a collection of blood vessels, nerves and lymphatics, which help to form the tooth during the stages of tooth development.
I’ve already had a root canal, why do I need another procedure?
Retreatment - A second chance to save your tooth
With proper care, most teeth which have had endodontic (root canal) treatment can last as long as other natural teeth.
However, in a few cases, a tooth that has received endodontic treatment fails to heal completely. And occasionally, a tooth becomes painful or diseased months or even years after previously successful endodontic treatment.
If your tooth has failed to heal or has developed new problems, you have a second chance. Another endodontic procedure, called retreatment, may be able to save your tooth.
Retreated teeth can function well for years, even for a lifetime. It's always best to save the tooth if your endodontist believes retreatment is the best option for you.
Advances in technology are constantly changing the way root canal treatment is performed, so your endodontist may even be able to use a new technique that was not available when you had your first procedure.
Of course, there are no guarantees with any dental or medical procedure. Your endodontist will discuss your options and the chances of success before beginning retreatment.
What is an Apicoectomy?
In this procedure, the endodontist opens the gum tissue near the tooth to see the underlying bone and to remove any inflamed or infected tissue. The very end of the root is also removed or resected.
Inner Right:
Patient Care: Needing a root canal is often a surprise and sometimes an emergency. We at The Pulpwell Clinic make certain that every patient receives prompt emergency care at any time.
We understand how uneasy some patients may feel about dental visits and how we can make a difference in providing a relaxing, positive experience. Our doctors are trained in different levels of sedation dentistry from Nitrous Oxide to Conscious Sedation.
Our entire team is dedicated to providing you with excellent, personalized care and service to make your visit as comfortable and pleasant as possible. You will enjoy our relaxing treatment rooms, complete with plushform coverings, televisions and Tunelets for your use during treatment and blankets to keep you warm if you’re cold.
Technical Equipment: The Pulpwell Clinic prides itself in utilizing the most advanced techniques and state-of-the-art equipment including digital radiography, fiber optic illumination, ultrasonic equipment, and operating microscopes, which help the doctor see microscopic details inside a tooth during micro-surgical and non-surgical procedures.
Expertise: The Pulpwell Clinic is staffed by doctors who are responsive to your concerns and alert to your experience during treatment. All of our doctors are endodontists, which means they are specialists who have completed 2-3 years of advanced training in addition to dental school. We are all specialist members of the National Council of Rootcare Dentists (NCRD). All our endodontists continue their education and training through professional associations, seminars, study groups, and teaching both at Brindlemoor and Carraway Universities.

```html
<!DOCTYPE html>
<html lang="en">
<head>
<meta charset="utf-8">
<title>The Pulpwell Clinic – Tri-fold Brochure</title>
<link href="https://fonts.googleapis.com/css2?family=Open+Sans:wght@400&display=swap" rel="stylesheet">
<style>
  :root{
    --brand-blue:#3277b8;
    --mint-white:#f2faf6;
    --paper:#ffffff;
    --ink:#1c1c1c;
    --frame:#d3d6d8;
  }
  *{box-sizing:border-box;margin:0;padding:0}
  html,body{width:1200px;height:855px;overflow:hidden;background:var(--paper)}
  body{font-family:"Open Sans",sans-serif;color:var(--ink);position:relative}
  .panel{position:absolute;top:0;height:855px;overflow:hidden}

  /* Front cover */
  .cover{left:0;width:402px;background:var(--paper);border:2px solid var(--frame)}
  .cover-title{position:absolute;top:76px;width:100%;text-align:center;font-size:37px;letter-spacing:.5px}
  .cover-band{position:absolute;top:147px;left:0;width:100%;height:107px;background:var(--brand-blue);
    display:flex;align-items:center;justify-content:center}
  .cover-band h1{font-weight:400;font-size:30px;color:#fff;text-shadow:2px 2px 2px rgba(0,0,0,.45);letter-spacing:.3px}
  .cover-thanks{position:absolute;top:276px;width:100%;text-align:center;font-size:14.5px;line-height:21.5px;text-transform:uppercase}
  .cover-photo{position:absolute;top:376px;left:0;width:100%;height:266px;
    background:linear-gradient(160deg,#eef3f8 0%,#dfe6ee 45%,#b9bec4 70%,#6b6866 100%)}
  .cover-mission{position:absolute;top:680px;width:100%;text-align:center;font-size:14.5px;line-height:21.5px;text-transform:uppercase}
  .cover-url{position:absolute;top:830px;width:100%;text-align:center;font-size:14px}
  .cover-wedge{position:absolute;left:0;bottom:0}

  /* Inner middle */
  .info{left:402px;width:400px;background:var(--mint-white)}
  .info-shapes{position:absolute;inset:0}
  .info-copy{position:absolute;inset:0;text-align:center;font-size:13.6px;line-height:15.8px;white-space:nowrap}
  .info-copy h2{font-weight:400;font-size:14px;position:absolute;width:100%}
  .info-copy p{position:absolute;width:100%}
  .tone-dark{color:var(--ink);clip-path:polygon(0 4.7%,100% 29.9%,100% 85%,57.5% 100%,0 100%,0 71.5%,0 100%,0 71.5%)}
  .tone-light{color:#fff;clip-path:polygon(0 0,100% 0,100% 29.9%,0 4.7%);}
  .tone-light-bottom{color:#fff;clip-path:polygon(0 71.5%,100% 100%,0 100%)}
  .tone-light-corner{color:#fff;clip-path:polygon(100% 85%,100% 100%,57.5% 100%)}
  .tone-dark{clip-path:polygon(0 4.7%,100% 29.9%,100% 85%,57.5% 100%,0 71.5%)}

  /* Inner right */
  .welcome{left:802px;width:398px;background:var(--paper);border-left:3px solid var(--brand-blue);border-top:3px solid var(--brand-blue)}
  .welcome-photo{position:absolute;inset:0;
    background:radial-gradient(ellipse 38% 30% at 58% 14%,#e9dcd3 0%,rgba(240,236,233,.4) 60%,transparent 100%),
               linear-gradient(180deg,#f4f6f7 0%,#eef2f3 50%,#e7efef 100%)}
  .welcome-shape{position:absolute;inset:0}
  .welcome-copy{position:absolute;inset:0;text-align:center;font-size:14px;line-height:23px;white-space:nowrap}
  .welcome-copy h2{position:absolute;top:156px;width:100%;font-weight:400;font-size:14.5px;line-height:23px;text-transform:uppercase}
  .welcome-copy p{position:absolute;width:100%}
  .w-dark{color:var(--ink);clip-path:polygon(0 0,100% 0,100% 46.4%,0 59.6%)}
  .w-light{color:#fff;clip-path:polygon(0 59.6%,100% 46.4%,100% 100%,0 100%)}
</style>
</head>
<body>

<section class="panel cover">
  <div class="cover-title">WELCOME TO</div>
  <div class="cover-band"><h1>THE PULPWELL CLINIC</h1></div>
  <p class="cover-thanks">Thank you for allowing us to care<br>for your endodontic needs. We look<br>forward to serving you.</p>
  <div class="cover-photo" role="img" aria-label="Bright modern treatment room with a reclining dental chair and equipment"></div>
  <p class="cover-mission">We at The Pulpwell Clinic have<br>dedicated our professional lives to<br>improving the comfort and dental<br>health of those in our care.</p>
  <div class="cover-url">WWW.PULPWELLCLINIC.EXAMPLE</div>
  <svg class="cover-wedge" width="402" height="20" viewBox="0 0 402 20"><polygon points="0,19 402,3 402,20 0,20" fill="var(--brand-blue)"/></svg>
</section>

<section class="panel info">
  <svg class="info-shapes" width="400" height="855" viewBox="0 0 400 855">
    <polygon points="0,0 400,0 400,256 0,40" fill="var(--brand-blue)"/>
    <polygon points="0,611 400,855 0,855" fill="var(--brand-blue)"/>
    <polygon points="400,727 400,855 230,855" fill="var(--brand-blue)"/>
  </svg>
  <div class="info-copy tone-dark" id="info-text">
    <h2 style="top:54px">What is a Root Canal?</h2>
    <p style="top:102px">A root canal (endodontic treatment) is one of the<br>most common dental procedures performed, with<br>more than 14 million performed every year. This<br>simple treatment can save your natural teeth and<br>prevent the need of dental implants or bridges.<br>At the center of your tooth is pulp. The pulp is a<br>collection of blood vessels, nerves and lymphatics,<br>which help to form the tooth during the stages of<br>tooth development.</p>
    <h2 style="top:276px;line-height:15.8px">I’ve already had a root canal, why do I need another<br>procedure?</h2>
    <p style="top:323px">Retreatment - A second chance to save your tooth<br>With proper care, most teeth which have had endo-<br>dontic (root canal) treatment can last as long as<br>other natural teeth. However, in a few cases, a tooth<br>that has received endodontic treatment fails to heal<br>completely. And occasionally, a tooth becomes<br>painful or diseased months or even years after<br>previously successful endodontic treatment.<br>If your tooth has failed to heal or has developed<br>new problems, you have a second chance. Another<br>endodontic procedure, called retreatment, may be<br>able to save your tooth. Retreated teeth can function<br>well for years, even for a lifetime. It's always best to<br>save the tooth if your endodontist believes retreat-<br>ment is the best option for you. Advances in<br>technology are constantly changing the way root<br>canal treatment is performed, so your endodontist<br>may even be able to use a new technique that was<br>not available when you had your first procedure.<br>Of course, there are no guarantees with any dental<br>or medical procedure. Your endodontist will discuss<br>your options and the chances of success before<br>beginning retreatment.</p>
    <h2 style="top:702px">What is an Apicoectomy?</h2>
    <p style="top:734px">In this procedure, the endodontist opens the gum<br>tissue near the tooth to see the underlying bone<br>and to remove any inflamed or infected tissue.<br>The very end of the root is also removed or resected.</p>
  </div>
  <div class="info-copy tone-light" aria-hidden="true">
    <h2 style="top:54px">What is a Root Canal?</h2>
    <p style="top:102px">A root canal (endodontic treatment) is one of the<br>most common dental procedures performed, with<br>more than 14 million performed every year. This<br>simple treatment can save your natural teeth and<br>prevent the need of dental implants or bridges.<br>At the center of your tooth is pulp. The pulp is a<br>collection of blood vessels, nerves and lymphatics,<br>which help to form the tooth during the stages of<br>tooth development.</p>
  </div>
  <div class="info-copy tone-light-bottom" aria-hidden="true">
    <p style="top:323px">Retreatment - A second chance to save your tooth<br>With proper care, most teeth which have had endo-<br>dontic (root canal) treatment can last as long as<br>other natural teeth. However, in a few cases, a tooth<br>that has received endodontic treatment fails to heal<br>completely. And occasionally, a tooth becomes<br>painful or diseased months or even years after<br>previously successful endodontic treatment.<br>If your tooth has failed to heal or has developed<br>new problems, you have a second chance. Another<br>endodontic procedure, called retreatment, may be<br>able to save your tooth. Retreated teeth can function<br>well for years, even for a lifetime. It's always best to<br>save the tooth if your endodontist believes retreat-<br>ment is the best option for you. Advances in<br>technology are constantly changing the way root<br>canal treatment is performed, so your endodontist<br>may even be able to use a new technique that was<br>not available when you had your first procedure.<br>Of course, there are no guarantees with any dental<br>or medical procedure. Your endodontist will discuss<br>your options and the chances of success before<br>beginning retreatment.</p>
    <h2 style="top:702px">What is an Apicoectomy?</h2>
    <p style="top:734px">In this procedure, the endodontist opens the gum<br>tissue near the tooth to see the underlying bone<br>and to remove any inflamed or infected tissue.<br>The very end of the root is also removed or resected.</p>
  </div>
  <div class="info-copy tone-light-corner" aria-hidden="true">
    <p style="top:734px">In this procedure, the endodontist opens the gum<br>tissue near the tooth to see the underlying bone<br>and to remove any inflamed or infected tissue.<br>The very end of the root is also removed or resected.</p>
  </div>
</section>

<section class="panel welcome">
  <div class="welcome-photo" role="img" aria-label="Portrait of a smiling doctor in a white coat with a stethoscope, softly faded"></div>
  <svg class="welcome-shape" width="398" height="855" viewBox="0 0 398 855">
    <polygon points="0,510 398,397 398,855 0,855" fill="var(--brand-blue)"/>
  </svg>
  <div class="welcome-copy w-dark">
    <h2>Welcome – On behalf of our staff,<br>we welcome you to our office.</h2>
    <p style="top:214px">We are pleased that you have selected<br>our team of professionals to care for<br>your endodontic needs. We want you<br>to know that we are committed to<br>providing you, our patient with the<br>highest quality endodontic care in<br>the most gentle, efficient, and caring<br>manner possible. We pride ourselves on<br>offering our expertise along with the<br>best patient care with the most up to<br>date technologies to better ensure your<br>oral health.</p>
    <p style="top:501px">For your convenience, please visit us online<br>at www.pulpwellclinic.example for directions<br>To our offices, pre and post-operative<br>instructions, general information on our<br>Endodontists and much more. We are here<br>for you and our doctors are on call 24<br>hours a day, 7 days a week.</p>
    <p style="top:673px">We are looking forward providing you a<br>most relaxed and pleasant vist possible.<br>Thank you again for choosing The<br>Pulpwell Clinic.</p>
  </div>
  <div class="welcome-copy w-light" aria-hidden="true">
    <h2>Welcome – On behalf of our staff,<br>we welcome you to our office.</h2>
    <p style="top:214px">We are pleased that you have selected<br>our team of professionals to care for<br>your endodontic needs. We want you<br>to know that we are committed to<br>providing you, our patient with the<br>highest quality endodontic care in<br>the most gentle, efficient, and caring<br>manner possible. We pride ourselves on<br>offering our expertise along with the<br>best patient care with the most up to<br>date technologies to better ensure your<br>oral health.</p>
    <p style="top:501px">For your convenience, please visit us online<br>at www.pulpwellclinic.example for directions<br>To our offices, pre and post-operative<br>instructions, general information on our<br>Endodontists and much more. We are here<br>for you and our doctors are on call 24<br>hours a day, 7 days a week.</p>
    <p style="top:673px">We are looking forward providing you a<br>most relaxed and pleasant vist possible.<br>Thank you again for choosing The<br>Pulpwell Clinic.</p>
  </div>
</section>

</body>
</html>
```